Rack Card for IV Infusion Vitamin Supplement bar

We need a very eye catching rack card so that customers would instantly know it is for IV vitamin infusions. We have our previous rack card (pdf) as an example that did not bring in any clients as an example as well as another one that we did not like too much. The bar is for people to feel better with hydration and vitamins.

Target Market(s)

Anyone

Industry/Entity Type

Healthcare

Requirements
Must have
• Logo on rack card
Should not have
• Not pink other than the logo

```html
<!DOCTYPE html>
<html lang="en">
<head>
<meta charset="utf-8">
<title>Verda Health &amp; Wellness – Rack Card</title>
<link rel="stylesheet" href="https://fonts.googleapis.com/css2?family=Montserrat:wght@400;500;700;800;900&display=swap">
<style>
  :root{
    --bg:#9a9a9a;
    --paper:#f0efea;
    --paper-light:#f8f7f3;
    --green:#0f4a3e;
    --blue:#2a9be0;
    --ink:#1b1b1b;
    --body:#333;
    --pink:#d9357f;
  }
  *{box-sizing:border-box;margin:0;padding:0}
  html,body{width:751px;height:1200px;overflow:hidden}
  body{background:var(--bg);font-family:"Montserrat",sans-serif;position:relative}

  .card{position:absolute;top:228px;width:330px;height:743px;background:var(--paper);overflow:hidden}
  .card--front{left:30px}
  .card--back{left:391px;background:linear-gradient(180deg,var(--paper-light),var(--paper))}
  .shapes{position:absolute;inset:0;width:330px;height:743px}

  /* front */
  .hero-photo{position:absolute;left:0;top:140px;width:330px;height:310px;
    background:radial-gradient(circle at 52% 60%,#f6a623 0 26%,transparent 27%),
               radial-gradient(circle at 85% 28%,#f7ad2c 0 22%,transparent 23%),
               linear-gradient(135deg,#6b5a48 0%,#a89f96 40%,#d8d5d1 100%)}
  .brand{position:absolute;top:22px;left:0;width:330px;text-align:center;color:var(--green)}
  .brand__mark{display:block;width:46px;height:46px;border-radius:50%;background:var(--pink);margin:0 auto 26px}
  .brand__name{font-weight:800;font-size:38px;letter-spacing:10px;line-height:1;padding-left:10px}
  .brand__tag{font-weight:800;font-size:9.5px;letter-spacing:4.6px;line-height:1;margin-top:5px;padding-left:5px}

  .headline{position:absolute;top:424px;left:0;width:330px;text-align:center;font-weight:900;line-height:45px;font-size:36px}
  .headline .blue{color:var(--blue)}
  .headline .green{color:var(--green);font-size:35px}

  .cta{position:absolute;top:567px;left:68px;width:190px;height:100px}
  .cta__word{position:absolute;font-weight:900;color:#fff;font-size:38px;line-height:1}
  .cta__book{left:38px;top:10px}
  .cta__now{left:50px;top:53px}

  .contact{position:absolute;top:683px;left:0;width:330px;text-align:center;color:#fff}
  .contact__phone{font-weight:700;font-size:15px}
  .contact__line{font-size:11px;margin-top:3px}
  .icon{display:inline-block;vertical-align:-1px;margin-right:3px}

  /* back */
  .menu{position:absolute;top:26px;left:21px;right:18px}
  .menu__title{color:var(--green);font-weight:900;font-size:18px;letter-spacing:.2px;margin-bottom:4px}
  .menu__title--addons{margin-top:12px}
  .item{margin-bottom:4px}
  .item__name{font-weight:800;font-size:12.6px;color:var(--ink);line-height:15px;position:relative;padding-left:9px}
  .item__name::before{content:"";position:absolute;left:0;top:4px;border-left:5px solid var(--green);border-top:4px solid transparent;border-bottom:4px solid transparent}
  .item__desc{font-size:9.4px;color:var(--body);line-height:12.2px;padding-left:10px}
  .item--tight{margin-bottom:2px}

  .footer-note{position:absolute;top:698px;left:0;width:330px;text-align:center;color:#fff;font-weight:500;font-size:14px;line-height:18px}
</style>
</head>
<body>

<section class="card card--front" aria-label="Rack card front">
  <div class="hero-photo" role="img" aria-label="Photo of sliced oranges with a vitamin ampoule and syringe on marble"></div>
  <svg class="shapes" viewBox="0 0 330 743" aria-hidden="true">
    <path d="M0 0H330V162Q170 168 0 198Z" fill="var(--paper-light)"/>
    <path d="M0 198Q170 168 330 162" fill="none" stroke="var(--green)" stroke-width="3"/>
    <path d="M0 440Q120 380 330 435V743H0Z" fill="var(--paper)"/>
    <path d="M0 440Q120 380 330 435" fill="none" stroke="var(--green)" stroke-width="3"/>
    <path d="M0 683Q150 640 330 686V743H0Z" fill="var(--green)"/>
    <path d="M0 675Q150 632 330 680" fill="none" stroke="var(--blue)" stroke-width="4"/>
  </svg>

  <div class="brand">
    <span class="brand__mark"></span>
    <div class="brand__name">VERDA</div>
    <div class="brand__tag">HEALTH &amp; WELLNESS</div>
  </div>

  <h1 class="headline">
    <span class="blue">VITAMIN</span><br>
    <span class="green">INFUSIONS AND</span><br>
    <span class="blue">INJECTIONS</span>
  </h1>

  <div class="cta">
    <svg width="190" height="100" viewBox="0 0 190 100" aria-hidden="true">
      <polygon points="28,2 188,0 162,48 4,54" fill="var(--green)" stroke="var(--blue)" stroke-width="2"/>
      <polygon points="36,48 174,44 152,88 96,92 86,100 80,93 50,95" fill="var(--blue)"/>
    </svg>
    <span class="cta__word cta__book">BOOK</span>
    <span class="cta__word cta__now">NOW</span>
  </div>

  <div class="contact">
    <div class="contact__phone"><svg class="icon" width="12" height="12" viewBox="0 0 12 12"><circle cx="6" cy="6" r="5.3" fill="none" stroke="#fff"/><path d="M4 3.5l1 1-.6.8a4 4 0 0 0 2.3 2.3l.8-.6 1 1-.8.9C5.8 8.7 3.3 6.2 3.1 4.3Z" fill="#fff"/></svg>555-018-2740</div>
    <div class="contact__line"><svg class="icon" width="11" height="11" viewBox="0 0 12 12"><circle cx="6" cy="6" r="5.3" fill="none" stroke="#fff"/><path d="M6 2.5a2 2 0 0 1 2 2c0 1.5-2 4-2 4s-2-2.5-2-4a2 2 0 0 1 2-2Z" fill="#fff"/></svg>1420 W. Elm St Suite 2B Riverton, IN 46000</div>
    <div class="contact__line"><svg class="icon" width="11" height="11" viewBox="0 0 12 12"><circle cx="6" cy="6" r="5.3" fill="none" stroke="#fff"/><path d="M1 6h10M6 1c-2.5 3-2.5 7 0 10M6 1c2.5 3 2.5 7 0 10" fill="none" stroke="#fff" stroke-width=".8"/></svg>www.verdatotalhealth.com</div>
  </div>
</section>

<section class="card card--back" aria-label="Rack card back">
  <svg class="shapes" viewBox="0 0 330 743" aria-hidden="true">
    <path d="M0 685Q165 650 330 688V743H0Z" fill="var(--green)"/>
    <path d="M0 680Q165 645 330 683" fill="none" stroke="var(--blue)" stroke-width="4"/>
  </svg>

  <div class="menu">
    <h2 class="menu__title">PREMIUM INFUSIONS</h2>
    <div class="item"><div class="item__name">VERDA COCKTAIL</div><p class="item__desc">Reduce stress, fatigue, and boost your energy. Verda client favorite! (IV fluids, Vitamin C, B-complex, B12, &amp; electrolytes)</p></div>
    <div class="item"><div class="item__name">IMMUNE SUPPORT</div><p class="item__desc">Protect the immune system when risk of illness is high. Great for pre, post-travel (IV fluids, Vitamin C, B-complex, and Zinc)</p></div>
    <div class="item"><div class="item__name">THE GLOW</div><p class="item__desc">Give a glowing boost to skin and hair from inside out. (IV fluids, Glutathione, Vitamin B-complex, and Biotin)</p></div>
    <div class="item"><div class="item__name">SPORTS RECOVERY</div><p class="item__desc">Recover fast from illness, exhaustion, and workouts. (IV fluids, B-complex, B12, and amino acids, and electrolytes)</p></div>
    <div class="item"><div class="item__name">ENERGIZED</div><p class="item__desc">Boost metabolism, burn fat easier, and feel energized. (IV fluids, B-complex, and amino acid blend)</p></div>
    <div class="item"><div class="item__name">BRAIN POWER</div><p class="item__desc">Support overall brain function, increase memory recall and improve certain aspects of learning. (IV fluids, B6, alpha lipoic acid, and taurine)</p></div>
    <div class="item item--tight"><div class="item__name">THE JETLAG DRIP</div></div>
    <div class="item item--tight"><div class="item__name">THE MIGRAINE / PMS DRIP</div></div>
    <div class="item item--tight"><div class="item__name">THE HANGOVER DRIP</div></div>
    <div class="item"><div class="item__name">NAD+ 125G/ 250G/ 500G DRIP</div><p class="item__desc">Enhance your cognitive health and help reverse aging. Promotes cell regeneration. Can aid mental clarity, better sleep, and energy.</p></div>
    <div class="item"><div class="item__name">HIGH DOSE VITAMIN C</div><p class="item__desc">*Medical clearance required</p></div>

    <h2 class="menu__title menu__title--addons">INFUSIONS ADD-ONS</h2>
    <div class="item"><div class="item__name">GLUTATHIONE</div><p class="item__desc">*A powerful natural antioxidant to help Detox</p></div>
    <div class="item item--tight"><div class="item__name">ADDITIONAL VITAMIN C</div></div>
    <div class="item item--tight"><div class="item__name">ADDITIONAL ZINC</div></div>
    <div class="item item--tight"><div class="item__name">ADDITIONAL MAGNESIUM</div></div>
    <div class="item item--tight"><div class="item__name">ANTI- INFLAMMATION MEDICATION</div></div>
    <div class="item item--tight"><div class="item__name">ADDITIONAL ZINC</div></div>
    <div class="item item--tight"><div class="item__name">ADDITIONAL MAGNESIUM</div></div>
    <div class="item item--tight"><div class="item__name">ANTI- INFLAMMATION MEDICATION</div></div>
  </div>

  <p class="footer-note">By appointments only,<br>including weekends <svg class="icon" width="12" height="12" viewBox="0 0 12 12"><circle cx="6" cy="6" r="5.3" fill="none" stroke="#fff"/><path d="M4 3.5l1 1-.6.8a4 4 0 0 0 2.3 2.3l.8-.6 1 1-.8.9C5.8 8.7 3.3 6.2 3.1 4.3Z" fill="#fff"/></svg>555-018-2740</p>
</section>

</body>
</html>
```